The Molar Compass (Cover Design for Ebook)

I need a cool and exciting eBook cover for my new book, launching very soon!
I want it to stand out and appeal to young professionals with big dreams.
It should be dramatic and bold and avoid cliche or generic photos. Simple design will work as long as it relates to the message of the book. The content will provide ten years of experience from working in the field and achieving success.
Title: The Molar Compass (at the top)
(Subheading Updated) The secrets to money, motivation and success they don’t teach you in dental school
OR The secrets to success they don't teach you in dental school.
OR The secrets to money, motivation and success
(smaller under title)
Author Updated: Dr K Fenwick (place at the bottom)
Updates

Target Market(s)

Ambitious young dentists
See instagram www.snapreel.com/themolarcompass for a sense of the style that I think could work.

Font styles to use
Serif
Sans Serif

Colors

Designer to choose colors to be used in the design.

Requirements
Must have
• Eye catching and cool.
• Show the benefits of success. Money, freedom, luxury
• Clear title and subheading
Nice to have
• Subtle dental reference
• dimensions 1600x2400
Should not have
• Boring photos of dentist/patients, dental clinic, teeth etc,

```html
<!DOCTYPE html>
<html lang="en">
<head>
<meta charset="utf-8">
<title>The Molar Compass – Cover</title>
<link rel="stylesheet" href="https://fonts.googleapis.com/css2?family=Roboto:ital,wght@0,100;0,300;0,400;0,700;0,900;1,900&display=swap">
<style>
  :root {
    --stage: #e9eaeb;
    --paper: #ffffff;
    --blue: #1a96d4;
    --blue-light: #5cc5f0;
    --blue-pale: #d6f0fb;
    --ink: #1c1f24;
    --navy: #1d2b3c;
  }
  * { margin: 0; padding: 0; box-sizing: border-box; }
  html, body {
    width: 1200px; height: 2250px; overflow: hidden;
    background: var(--stage);
    font-family: "Roboto", Arial, sans-serif;
  }
  .cover {
    position: absolute; left: 100px; top: 477px;
    width: 1000px; height: 1296px; overflow: hidden;
    background: radial-gradient(ellipse at 45% 25%, #ffffff 0%, #f7f6f4 45%, #eef3f7 100%);
    box-shadow: 22px 26px 40px rgba(0,0,0,0.35);
  }
  .cover__backdrop {
    position: absolute; left: 0; right: 0; bottom: 0; height: 560px;
    background: linear-gradient(160deg, rgba(214,240,251,0) 0%, rgba(170,223,247,0.7) 55%, #2aace6 100%);
  }
  .emblem {
    position: absolute; left: 300px; top: 100px;
    width: 400px; height: 380px;
    background: linear-gradient(180deg, var(--blue-pale) 0%, #a8dcf4 100%);
  }
  .title { position: absolute; left: 0; right: 0; top: 500px; text-align: center; color: var(--blue); }
  .title__the { display: block; font-weight: 100; font-size: 96px; line-height: 1; letter-spacing: 2px; }
  .title__main { display: block; font-weight: 900; font-size: 150px; line-height: 1; margin-top: 6px; letter-spacing: 1px; }
  .title__sub { display: block; font-weight: 400; font-size: 86px; line-height: 1; letter-spacing: 44px; margin-top: 34px; padding-left: 44px; }
  .subtitle { position: absolute; left: 0; right: 0; top: 925px; text-align: center; color: var(--ink); font-size: 35px; line-height: 1.4; font-weight: 300; }
  .subtitle strong { font-weight: 700; }
  .author { position: absolute; left: 0; right: 0; top: 1170px; text-align: center; color: var(--navy); font-weight: 900; font-style: italic; font-size: 44px; letter-spacing: 0.5px; }
</style>
</head>
<body>
  <main class="cover">
    <div class="cover__backdrop" role="img" aria-label="Flowing light blue wave background"></div>

    <div class="emblem" role="img" aria-label="Tooth emblem"></div>

    <h1 class="title">
      <span class="title__the">THE</span>
      <span class="title__main">MOLAR</span>
      <span class="title__sub">COMPASS</span>
    </h1>

    <p class="subtitle">The Secrets to<br><strong>Money, Motivation</strong> and <strong>Success</strong></p>

    <p class="author">KIERAN FENWICK</p>
  </main>
</body>
</html>
```